Menu Design Project for New Catering company

I would like to see my menus in a warm, inviting format. I prepare food for small intimate dinners, business lunches, picnics, parties, weddings and rehearsal dinners. I work with clients to help create their dream whether it includes items on my menu or to prepare very personal dishes that bring them warm memories of a special time or moment.

Target Market(s)

Organizations, wedding and or event planners

Industry/Entity Type

Catering

Requirements
Must have
• I would like to include the logo that is included in the attachment below. I also included a copy of the poster Lex Doyle created for me. I hope this helps. Please be creative. I am a very happy, cheerful person that enjoys cooking and having fun. I would like the design to represent my personality as well as my food. When I cater I treat my customers like an extension of my family and it comes across to them with everything I do for them. I hope this can somehow be reflected in your designs.
Should not have
• I'm open to all ideas and don't want to limit your creativity.

```html
<!DOCTYPE html>
<html lang="en">
<head>
<meta charset="utf-8">
<title>Boxed Lunch Menu Options</title>
<link href="https://fonts.googleapis.com/css2?family=Arimo:wght@400;700&family=Playball&display=swap" rel="stylesheet">
<style>
  :root{
    --green:#2e9a48;
    --green-dark:#1f7a36;
    --ink:#1b1b1b;
    --grey:#5f6b63;
    --paper:#ffffff;
    --frame:#8cc79a;
  }
  html,body{margin:0;padding:0;overflow:hidden;background:var(--paper);}
  .menu{
    position:relative;width:776px;height:1200px;overflow:hidden;
    background:var(--paper);font-family:"Arimo",Arial,sans-serif;color:var(--ink);
  }
  .menu-title{
    margin:0;position:absolute;top:4px;left:0;width:100%;text-align:center;
    font-family:"Playball",cursive;font-weight:400;font-size:44px;line-height:66px;color:#3b2a22;
  }
  .menu-box{
    position:absolute;top:80px;left:34px;width:676px;height:738px;
    border:2px solid var(--frame);padding:6px 14px 14px;
  }
  .intro{margin:0 0 12px;font-size:15.5px;font-weight:700;line-height:22px;max-width:650px;}
  .intro .lead{color:var(--green);}
  .item{margin:0 0 13px;max-width:600px;}
  .item-name{margin:0;color:var(--green);font-weight:700;font-size:15.5px;line-height:23px;}
  .item-desc{margin:0;font-weight:700;font-size:15.5px;line-height:23px;}
  .dressings{margin:0 0 16px;font-size:15.5px;font-weight:700;line-height:23px;}
  .dressings .label{color:var(--green);}
  .drinks{display:flex;justify-content:space-between;font-size:16px;font-weight:700;line-height:23px;margin:0 0 8px;}
  .drinks .label{color:var(--green);}
  .drinks .price{color:var(--green);}
  .note{margin:0 0 8px;font-size:11px;font-weight:700;line-height:16px;}
  .brand{
    position:absolute;top:866px;left:0;width:100%;
    display:flex;flex-direction:column;align-items:center;gap:10px;
  }
  .brand-dot{width:100px;height:100px;border-radius:50%;background:var(--green);}
  .brand-name{font-size:32px;line-height:38px;font-weight:700;color:var(--grey);letter-spacing:.5px;}
  .footer-text{
    position:absolute;top:1074px;left:28px;width:720px;margin:0;text-align:center;
    font-size:15.5px;font-weight:700;line-height:22px;
  }
  .footer-text .accent{color:var(--green);}
  .footer-band{position:absolute;left:0;bottom:0;width:100%;height:24px;background:var(--green-dark);}
</style>
</head>
<body>
<main class="menu">
  <h1 class="menu-title">Boxed Lunch Menu Options</h1>

  <section class="menu-box">
    <p class="intro"><span class="lead">BOX LUNCHES</span> – Served with chips, choice of fruit cup or side salad, also included choice of cookie or cupcake. Drinks sold separately.</p>

    <div class="item">
      <p class="item-name">Malibu Chicken</p>
      <p class="item-desc">Grilled chicken breast, topped with sweet honey baked ham, Swiss cheese and served on a fresh croissant with a side of rich sweet mustard sauce</p>
    </div>
    <div class="item">
      <p class="item-name">Italian Meatball with Mozzarella Cheese</p>
      <p class="item-desc">In a rich marinara sauce served on a fresh Hoagie Bun</p>
    </div>
    <div class="item">
      <p class="item-name">Grilled Hawaiian Chicken Sandwich</p>
      <p class="item-desc">Grilled chicken topped with a sweet grilled pineapple ring and guacamole sauce on a fresh Hawaiian bun or croissant</p>
    </div>
    <div class="item">
      <p class="item-name">Honey Chicken Salad</p>
      <p class="item-desc">A fresh chicken salad filled with grapes, crispy celery, pecans, shredded chicken-served on a fresh croissant</p>
    </div>
    <div class="item">
      <p class="item-name">Honey Baked Ham and Swiss Cheese</p>
      <p class="item-desc">piled high on a fresh croissant (with choices of - lettuce, tomato slice, onions and mayo/salad dressing)e</p>
    </div>
    <div class="item">
      <p class="item-name">Ultimate BLT with Avocado and Spicy Mayo</p>
      <p class="item-desc">Crispy bacon, lettuce, tomato, thin slices of red onion, avocado slices atop toasted bread with spicy mayo.</p>
    </div>
    <div class="item">
      <p class="item-name">Spinach Salad with Bacon Dressing</p>
      <p class="item-desc">Baby Spinach, mushrooms, red onions and sliced boiled eggs served with croissant and bacon dressing.</p>
    </div>

    <p class="dressings"><span class="label">Salad Dressing Choices:</span> Ranch, Italian, Honey Mustard or Blue Cheese</p>

    <p class="drinks"><span><span class="label">Drinks:</span> 12 oz. soft drinks or 16 oz. bottled water</span><span class="price">$1.00 each</span></p>

    <p class="note">NOTE: A delivery fee of $20.00 will be assessed for orders totaling less than $150.00</p>
    <p class="note">Please send your order to my e-mail address at least 24 Hours in advance also include time requested, address and contact information (including phone number)—I will send you a confirmation that the order has been received and invoiced day of delivery.</p>
  </section>

  <div class="brand">
    <div class="brand-dot"></div>
    <div class="brand-name">Bright Thyme</div>
  </div>

  <p class="footer-text">Please let me know if there is any way I can help you in the future. You may contact me with e-mail at <span class="accent">mara@brightthyme.com</span> or call my cell phone <span class="accent">@ 555-014-2287</span>. We look forward to building a relationship with you and hope to hear from you soon! Check back frequently for updates to our website. There's much more to come!</p>

  <div class="footer-band"></div>
</main>
</body>
</html>
```